LUMO Electrical Services Letter Head

I need a professional clean looking design that will incorporate my company logo and information such as postal address, website, contact email "service@lumoelectrical.com.au" and phone number.

somewhere on the document i will also require my electrical contractor number "EC 047362" and my Australian Business number "57 193 640 208" these have to legally be on the document so they dont need to be a main feature, maybe in the footer in a smaller text.

Can you also have the 3 blue dashes from my logo as the watermark.

I would like the colour scheme to match my logo, business card and website www.lumoelectrical.com.au

I have the JPEG and PNG files for my logo which it will not allow me to upload as they are too wide, if you require these please let me know.

Target Market(s)

To be used for quotes and letters to commercial clients

Industry/Entity Type

Electric Company

Colors
0555a3
3176b5
85acd3
cfdfed
eaf1f7

Requirements
Must have
• company logo and information such as postal address, website, contact email "service@lumoelectrical.com.au" and phone number.
• somewhere on the document i will also require my electrical contractor number "EC 047362" and my Australian Business number "57 193 640 208" these have to legally be on the document so they dont need to be a main feature, maybe in the footer in a smaller text.
• I would like the colour scheme to match my logo, business card and website www.lumoelectrical.com.au
Nice to have
• Can you also have the 3 blue dashes from my logo as the watermark.

```html
<!DOCTYPE html>
<html lang="en">
<head>
<meta charset="utf-8">
<title>LUMO Electrical Services – Letterhead</title>
<link href="https://fonts.googleapis.com/css2?family=Lato:wght@400;700&family=Source+Sans+3:wght@400;600;700&display=swap" rel="stylesheet">
<style>
  :root {
    --brand-blue: #0555a3;
    --accent-blue: #1f8fd6;
    --mid-blue: #3176b5;
    --ink: #231f20;
    --body-ink: #2b2b2b;
    --muted: #6d6e71;
    --paper: #ffffff;
    --footer-band: #1d1d1f;
  }
  * { margin: 0; padding: 0; box-sizing: border-box; }
  html, body { width: 869px; height: 1200px; overflow: hidden; }
  body { background: var(--paper); font-family: "Source Sans 3", "Myriad Pro", sans-serif; color: var(--body-ink); }

  .letterhead { position: relative; width: 869px; height: 1200px; background: var(--paper); }

  .contact-block {
    position: absolute; left: 140px; top: 95px;
    display: grid; grid-template-columns: 72px auto; column-gap: 0;
    font-family: "Lato", sans-serif; font-size: 10.5px; line-height: 12.5px;
  }
  .contact-labels { color: var(--accent-blue); padding-top: 8px; }
  .contact-values { color: var(--muted); }
  .contact-values .company { color: var(--accent-blue); font-weight: 700; }

  .brand {
    position: absolute; right: 150px; top: 118px; text-align: right;
  }
  .brand-name {
    display: flex; align-items: center; gap: 8px;
    font-family: "Source Sans 3", sans-serif; font-weight: 700;
    font-size: 19px; color: var(--ink); letter-spacing: 0.2px;
  }
  .brand-mark { width: 14px; height: 14px; background: var(--mid-blue); }
  .abn { font-family: "Lato", sans-serif; font-size: 9px; color: var(--ink); margin-top: 6px; }
  .abn span { color: var(--accent-blue); }

  .recipient {
    position: absolute; right: 152px; top: 303px; text-align: right;
    font-size: 12px; line-height: 15.3px; color: var(--body-ink);
  }

  .letter-body {
    position: absolute; left: 140px; width: 578px; top: 455px;
    font-size: 12.4px; line-height: 15.4px; text-align: justify; color: var(--body-ink);
  }
  .letter-body p { text-indent: 37px; margin-bottom: 15.4px; }

  .signature { position: absolute; left: 141px; top: 1000px; }
  .signature .name { font-weight: 700; font-size: 16px; color: var(--brand-blue); }
  .signature .role { font-size: 16px; color: var(--muted); margin-top: 1px; }

  .footer-band {
    position: absolute; left: 0; right: 0; bottom: 40px; height: 48px;
    background: var(--footer-band); display: flex; align-items: center; padding-left: 80px;
  }
  .contractor-no { font-family: "Lato", sans-serif; font-size: 17px; color: #ffffff; letter-spacing: 0.5px; }
</style>
</head>
<body>
<main class="letterhead">
  <header>
    <div class="contact-block">
      <div class="contact-labels">
        <div>Phone :</div><div>Address:</div><div>E-mail:</div><div>Web:</div>
      </div>
      <div class="contact-values">
        <div class="company">LUMO Electrical Services</div>
        <div>(08) 6124 5079</div>
        <div>P.O Box 3819, Harbourside North WA 6172</div>
        <div>jordan@lumoelectrical.com.au</div>
        <div>www.lumoelectrical.com.au</div>
      </div>
    </div>
    <div class="brand">
      <div class="brand-name"><span class="brand-mark"></span>LUMO Electrical Services</div>
      <div class="abn">ABN: <span>57 193 640 208</span></div>
    </div>
  </header>

  <address class="recipient" style="font-style:normal">
    Mr. lorem lorem<br>Commercial Director<br>2750 Meadow Ridge Road<br>Fairlane, Mo 65790
  </address>

  <section class="letter-body">
    <p>Lorem ipsum dolor sit amet, consectetur adipiscing elit. Suspendisse condimentum egestas tellus et viverra. Vestibulum euismod lacus eget nisi ornare, id laoreet tortor dapibus. Donec lacinia euismod diam, convallis tempus risus. Ut et felis tempor eros blandit feugiat ut non enim. In vestibulum ligula blandit magna blandit dictum. Sed malesuada erat id mauris pretium, eget congue felis interdum. Aenean ultricies enim nec lorem vestibulum, nec commodo quam sagittis. Cras bibendum, mauris eget aliquet semper, libero ipsum ultricies nunc, euismod pellentesque orci risus sit amet nibh. Maecenas feugiat mi a metus convallis pharetra.</p>
    <p>Duis porta, turpis ut pulvinar hendrerit, elit lorem vehicula turpis, lacinia semper purus eros ac nisi. Sed consectetur ante scelerisque tortor pellentesque imperdiet. Pellentesque habitant morbi tristique senectus et netus et malesuada fames ac turpis egestas. Quisque justo turpis, varius id ante nec, accumsan ultricies magna. Mauris lorem lectus, dignissim nec felis a, tincidunt pharetra tellus. Donec non euismod est. Nulla in elit quis tellus mattis feugiat vitae ut magna. Etiam at nisi quis dolor lacinia hendrerit placerat et risus. Vestibulum ac sapien ut justo varius venenatis.</p>
    <p>Donec eget nunc bibendum, sodales augue vel, dapibus nibh. Praesent mollis urna vel enim gravida aliquet nec non ipsum. Lorem ipsum dolor sit amet, consectetur adipiscing elit. Class aptent taciti sociosqu ad litora torquent per conubia nostra, per inceptos himenaeos. Phasellus et dolor ac nulla auctor consequat malesuada sit amet diam. Mauris a nunc neque. Etiam aliquet ligula in rhoncus sagittis.</p>
    <p>Sed luctus nibh erat, non varius augue vehicula ut. Nam diam est, sollicitudin in ligula vel, aliquam faucibus neque. Etiam luctus tempus ultricies. Duis posuere lobortis placerat. Suspendisse porttitor, orci eu scelerisque commodo, augue metus dictum nisl, eget facilisis mi ligula imperdiet ligula. Aenean ornare dui eu viverra ullamcorper. Etiam sed venenatis ante, id condimentum mauris. Suspendisse lobortis, ante quis suscipit pharetra, nulla ipsum malesuada mi, vitae molestie tellus velit ac sapien.</p>
    <p>Mauris vitae orci augue. Duis sit amet erat id lectus sollicitudin dignissim lacinia a lectus. Aenean ac luctus massa. Mauris vitae convallis arcu, id fringilla mauris. Aenean auctor dictum tellus et volutpat. Nullam est velit, hendrerit non pretium quis, convallis gravida tortor. Morbi tempus convallis enim, ut iaculis tortor posuere vel. Etiam orci nunc, euismod in congue blandit, laoreet nec tellus. Mauris faucibus justo a odio tristique, vitae lacinia ipsum porta. Praesent massa turpis, lobortis non augue sit amet, molestie mattis sapien. Nunc elementum dolor a dui venenatis accumsan. In consequat lobortis vestibulum.</p>
  </section>

  <div class="signature">
    <div class="name">Jordan Hale</div>
    <div class="role">Proprietor</div>
  </div>

  <footer class="footer-band">
    <span class="contractor-no">EC 047362</span>
  </footer>
</main>
</body>
</html>
```